Law Firm Business Card

This is a business card for a law firm that serves US military and veterans.

The card must have ONLY the following (we want an uncluttered look):

- Company logo (PNG, GIF, JPEG copies uploaded)
- A tagline reading: "a law firm for service members and veterans"
- My name and title: "Martin Okello" and "Attorney"
- My email: "martin.okello@harborlinecounsel.com"
- My number: "855-FILE-NOW (345-3669)"

We are looking for a clean, simple layout with only the above information, likely printed on a bright white cotton stock. The font of our logo is DIN 1451, and the font used on our website is Helvetica Neue. The color of our logo is #336699, and we probably want the tagline in that color also, and my contact information in a dark grey. Please review our website at www.harborlinecounsel.com to ensure your card design complements our website style.

Thanks and we look forward to seeing your submissions.

A few notes:

- Two-sided submissions are ok
- Please don't add graphics (scales of justice, judges hammer, etc)

```html
<!DOCTYPE html>
<html lang="en">
<head>
<meta charset="utf-8">
<title>Harborline Counsel – Business Card</title>
<link rel="stylesheet" href="https://fonts.googleapis.com/css2?family=Oswald:wght@600;700&family=Roboto:wght@500&display=swap">
<style>
  :root {
    --brand-blue: #336699;
    --card-white: #ffffff;
    --ink-grey: #3a3a3a;
    --backdrop: #e4e4e4;
  }
  * { box-sizing: border-box; margin: 0; padding: 0; }
  html, body {
    width: 1200px;
    height: 900px;
    overflow: hidden;
    background: var(--backdrop);
  }
  .card {
    position: absolute;
    left: 75px;
    top: 150px;
    width: 1050px;
    height: 600px;
    background: var(--card-white);
    box-shadow: 0 6px 24px rgba(0,0,0,0.12);
    overflow: hidden;
  }
  .firm-mark {
    position: absolute;
    top: 78px;
    left: 0;
    width: 100%;
    display: flex;
    justify-content: center;
    align-items: center;
    gap: 16px;
  }
  .firm-mark__square {
    width: 26px;
    height: 26px;
    background: var(--brand-blue);
    flex: none;
  }
  .firm-mark__name {
    font-family: "Oswald", sans-serif;
    font-weight: 600;
    font-size: 46px;
    line-height: 1;
    letter-spacing: 3px;
    color: var(--brand-blue);
  }
  .tagline {
    position: absolute;
    top: 170px;
    left: 0;
    width: 100%;
    text-align: center;
    font-family: "Roboto", sans-serif;
    font-weight: 500;
    font-size: 23px;
    letter-spacing: 4px;
    color: var(--brand-blue);
  }
  .name-band {
    position: absolute;
    top: 218px;
    left: 0;
    width: 100%;
    height: 175px;
    background: var(--brand-blue);
    text-align: center;
    color: var(--card-white);
    font-family: "Oswald", sans-serif;
    font-weight: 700;
  }
  .name-band__name {
    display: block;
    margin-top: 24px;
    font-size: 44px;
    line-height: 1.2;
    letter-spacing: 9px;
  }
  .name-band__title {
    display: block;
    margin-top: 6px;
    font-size: 32px;
    line-height: 1.2;
    letter-spacing: 7px;
  }
  .contact-list {
    position: absolute;
    left: 95px;
    top: 440px;
    list-style: none;
  }
  .contact-list__item {
    display: flex;
    align-items: center;
    gap: 24px;
    height: 64px;
    font-family: "Oswald", sans-serif;
    font-weight: 600;
    font-size: 30px;
    letter-spacing: 5px;
    color: var(--ink-grey);
  }
  .contact-icon {
    width: 40px;
    height: 40px;
    flex: none;
  }
</style>
</head>
<body>
  <main class="card">
    <h1 class="firm-mark">
      <span class="firm-mark__square" aria-hidden="true"></span>
      <span class="firm-mark__name">Harborline Counsel</span>
    </h1>
    <p class="tagline">A Law Firm for Service Members and Veterans.</p>

    <section class="name-band">
      <span class="name-band__name">Martin Okello</span>
      <span class="name-band__title">Attorney</span>
    </section>

    <ul class="contact-list">
      <li class="contact-list__item">
        <svg class="contact-icon" viewBox="0 0 40 40" aria-hidden="true">
          <circle cx="20" cy="20" r="17" fill="none" stroke="#3a3a3a" stroke-width="2.5"/>
          <path d="M14 11c1.5-1 2.6-.6 3.4.8l1.4 2.6c.6 1.1.3 2-.7 2.7l-1 .7c.9 2.3 2.6 4.1 4.9 5l.7-1c.7-1 1.6-1.3 2.7-.7l2.6 1.4c1.4.8 1.8 1.9.8 3.4-1.2 1.8-3.2 2.6-5.3 1.9-5.2-1.8-9.3-5.9-11.1-11.1-.7-2.1.1-4.1 1.6-5.7z" fill="#3a3a3a"/>
        </svg>
        <span>855-FILE-NOW (345-3669)</span>
      </li>
      <li class="contact-list__item">
        <svg class="contact-icon" viewBox="0 0 40 40" aria-hidden="true">
          <circle cx="20" cy="20" r="17" fill="none" stroke="#3a3a3a" stroke-width="2.5"/>
          <rect x="10" y="13" width="20" height="14" rx="1.5" fill="none" stroke="#3a3a3a" stroke-width="2.2"/>
          <path d="M10.5 14l9.5 7.5 9.5-7.5" fill="none" stroke="#3a3a3a" stroke-width="2.2" stroke-linejoin="round"/>
        </svg>
        <span>martin.okello@harborlinecounsel.com</span>
      </li>
    </ul>
  </main>
</body>
</html>
```